Help me create an amazing cover for my first ebook!!

I am looking to have a modern and professional looking cover for my first ebook. It will be published through Borvex Quill Self Press and will need to follow their formatting and guidelines. I want the cover to have a modern and vibrant feel, that appeals to a millennial audience. This is a real estate book that is focused on a niche category catered to young professionals, so the idea would be to appeal to them.

Title:
The Twentysomething Playbook for Duplex Living

A Smart Property Buying Plan to Start Early, Cut Your Housing Costs (Sometimes to Zero), and Speed Up Your Path to Lasting Wealth.

Davin Osterlund

Target Market(s)

Real Estate investors, investors, millennials, young professionals, college educated, 20-40 years old.Financial freedom, finance.

Industry/Entity Type

Real Estate

Font styles to use
Sans Serif

Colors

Designer to choose colors to be used in the design.

Requirements
Must have
• Must follow the borvex quill self press format. I attached a screenshot of the details, it can also be found here: https://qsp.borvexbooks.example/en_US/help/topic/R481736025
• Must include this title:
• The Twentysomething Playbook for Duplex Living
• A Smart Property Buying Plan to Start Early, Cut Your Housing Costs (Sometimes to Zero), and Speed Up Your Path to Lasting Wealth.
• Davin Osterlund.
• I added examples of book covers I like to use as a guide, I also added some color pallette examples.
Nice to have
• Modern, clean design that's not too busy. Some sort of simple photo or illustration to incorporate in the cover along with the text would be nice.

```html
<!DOCTYPE html>
<html lang="en">
<head>
<meta charset="utf-8">
<title>The Twentysomething Playbook for Duplex Living — Cover Concepts</title>
<link rel="stylesheet" href="https://fonts.googleapis.com/css2?family=Anton&family=Open+Sans:wght@400;700&family=Quicksand:wght@300;400;700&display=swap">
<style>
  :root {
    --stage: #ececec;
    --night-core: #2b2b2b;
    --night-edge: #0a0a0a;
    --sky-blue: #0aa9e8;
    --rule-grey: #4a4a4a;
    --teal-core: #25404b;
    --teal-edge: #13252d;
    --ember: #ff7a00;
    --paper: #ffffff;
  }
  * { margin: 0; padding: 0; box-sizing: border-box; }
  html, body {
    width: 1200px; height: 901px; overflow: hidden;
    background: var(--stage);
  }
  .stage { position: relative; width: 1200px; height: 901px; }
  .cover { position: absolute; top: 0; height: 901px; overflow: hidden; }
  .cover--midnight { left: 0; width: 560px; }
  .cover--teal { left: 636px; width: 564px; }
  .cover svg { display: block; width: 100%; height: 100%; }

  .thin-title { font-family: 'Quicksand', sans-serif; font-weight: 300; fill: var(--sky-blue); }
  .body-copy { font-family: 'Open Sans', sans-serif; font-weight: 400; fill: var(--paper); }
  .body-copy--accent { fill: var(--sky-blue); }
  .author--midnight { font-family: 'Quicksand', sans-serif; font-weight: 400; fill: var(--sky-blue); letter-spacing: 2px; }

  .bold-title { font-family: 'Anton', sans-serif; fill: var(--ember); }
  .round-title { font-family: 'Quicksand', sans-serif; font-weight: 700; fill: var(--paper); }
  .bold-copy { font-family: 'Open Sans', sans-serif; font-weight: 700; fill: var(--paper); }
  .bold-copy--accent { fill: var(--ember); }
  .author--teal { font-family: 'Anton', sans-serif; fill: var(--ember); }
</style>
</head>
<body>
<main class="stage">

  <section class="cover cover--midnight" aria-label="Cover concept, dark blue version">
    <svg viewBox="0 0 560 901" xmlns="http://www.w3.org/2000/svg">
      <defs>
        <radialGradient id="nightGlow" cx="50%" cy="45%" r="70%">
          <stop offset="0" stop-color="#2b2b2b"/>
          <stop offset="1" stop-color="#0a0a0a"/>
        </radialGradient>
        <linearGradient id="roofTone" x1="0" y1="0" x2="0" y2="1">
          <stop offset="0" stop-color="#0aa9e8"/>
          <stop offset="1" stop-color="#0a6f99"/>
        </linearGradient>
      </defs>
      <rect width="560" height="901" fill="url(#nightGlow)"/>

      <text class="thin-title" x="280" y="78" text-anchor="middle" font-size="48" textLength="500" lengthAdjust="spacingAndGlyphs">The Twentysomething</text>

      <rect x="0" y="137" width="92" height="3" fill="var(--rule-grey)"/>
      <rect x="0" y="143" width="92" height="3" fill="var(--rule-grey)"/>
      <rect x="468" y="137" width="92" height="3" fill="var(--rule-grey)"/>
      <rect x="468" y="143" width="92" height="3" fill="var(--rule-grey)"/>
      <text class="thin-title" x="280" y="166" text-anchor="middle" font-size="58" textLength="350" lengthAdjust="spacingAndGlyphs">Playbook for</text>

      <rect class="house-art" x="130" y="192" width="300" height="106" rx="4" fill="url(#roofTone)" opacity="0.85"
            role="img" aria-label="Line illustration of a house roof with a small window"/>

      <text class="thin-title" x="280" y="388" text-anchor="middle" font-size="108">Duplex</text>
      <text class="thin-title" x="280" y="484" text-anchor="middle" font-size="108">LIVING</text>

      <rect x="12" y="497" width="526" height="2" fill="var(--rule-grey)"/>

      <text class="body-copy" x="280" y="576" text-anchor="middle" font-size="24">A Smart Property Buying Plan to</text>
      <text class="body-copy body-copy--accent" x="280" y="610" text-anchor="middle" font-size="24">Start Early</text>

      <text class="body-copy" x="280" y="692" text-anchor="middle" font-size="22">Cut Your Housing Costs (Sometimes to Zero),</text>
      <text class="body-copy" x="280" y="723" text-anchor="middle" font-size="22">and Speed Up Your Path to Lasting Wealth</text>

      <rect x="12" y="789" width="526" height="2" fill="var(--rule-grey)"/>

      <text class="author--midnight" x="280" y="868" text-anchor="middle" font-size="54">Davin Osterlund</text>
    </svg>
  </section>

  <section class="cover cover--teal" aria-label="Cover concept, orange and teal version">
    <svg viewBox="0 0 564 901" xmlns="http://www.w3.org/2000/svg">
      <defs>
        <radialGradient id="tealGlow" cx="50%" cy="40%" r="75%">
          <stop offset="0" stop-color="#25404b"/>
          <stop offset="1" stop-color="#13252d"/>
        </radialGradient>
        <linearGradient id="rooftops" x1="0" y1="0" x2="0" y2="1">
          <stop offset="0" stop-color="#ff7a00"/>
          <stop offset="0.7" stop-color="#f08a2a"/>
          <stop offset="1" stop-color="#f4f4f4"/>
        </linearGradient>
      </defs>
      <rect width="564" height="901" fill="url(#tealGlow)"/>

      <rect x="0" y="30" width="200" height="26" fill="var(--ember)"/>
      <rect x="344" y="30" width="220" height="26" fill="var(--ember)"/>
      <text class="round-title" x="272" y="62" text-anchor="middle" font-size="56">The</text>

      <text class="bold-title" x="282" y="140" text-anchor="middle" font-size="64" textLength="420" lengthAdjust="spacingAndGlyphs">Twentysomething</text>
      <text class="round-title" x="282" y="188" text-anchor="middle" font-size="40">Playbook for</text>
      <text class="bold-title" x="282" y="264" text-anchor="middle" font-size="72" textLength="440" lengthAdjust="spacingAndGlyphs">Duplex Living</text>

      <rect x="14" y="285" width="534" height="2" fill="var(--paper)" opacity="0.85"/>

      <text class="bold-copy" x="282" y="340" text-anchor="middle" font-size="27">A Smart Property Buying Plan</text>
      <rect x="14" y="373" width="34" height="2" fill="var(--paper)"/>
      <rect x="516" y="373" width="34" height="2" fill="var(--paper)"/>
      <text class="bold-copy" x="282" y="384" text-anchor="middle" font-size="27">to <tspan class="bold-copy--accent">Start Early</tspan></text>

      <rect class="rooftops-art" x="12" y="420" width="536" height="296" rx="6" fill="url(#rooftops)" opacity="0.9"
            role="img" aria-label="Illustration of three orange house rooftops with windows above a white swoosh"/>

      <text class="bold-copy" x="282" y="750" text-anchor="middle" font-size="22">Cut Your Housing Costs (Sometimes to Zero),</text>
      <text class="bold-copy" x="282" y="780" text-anchor="middle" font-size="22">and Speed Up Your Path to Lasting Wealth</text>

      <rect x="14" y="799" width="534" height="2" fill="var(--paper)" opacity="0.85"/>

      <text class="author--teal" x="282" y="874" text-anchor="middle" font-size="56">Davin Osterlund</text>
    </svg>
  </section>

</main>
</body>
</html>
```